Willowmere Loft B&B Business Card

This beautiful high-class B&B is looking for a business card that stands out from the rest. They are in the middle of the countryside, have chickens, geese and a dog. They also love bumble bees.

I was maybe thinking a rustic drawing / print of a bumble bee and a sketch of the house, I am not sure.. I quite like the feel of this... http://www.tarnwick-mill.co.uk/

Industry/Entity Type

Business

Contact Information for Business Card

Willowmere Loft
Bed & Breakfast
Brackleford, Hensworth, Somerset, TA14 7QP
01632 960418 | www.willowmereloft.co.uk

```html
<!DOCTYPE html>
<html lang="en">
<head>
<meta charset="utf-8">
<title>Willowmere Loft B&amp;B — Business Card</title>
<link href="https://fonts.googleapis.com/css2?family=Cormorant+Garamond:wght@500;600&family=EB+Garamond:ital@1&display=swap" rel="stylesheet">
<style>
  :root {
    --backdrop: #ececec;
    --cream: #e7d9a4;
    --umber: #4a1d15;
    --gold: #c98a2a;
    --ink: #3e2a1c;
    --ink-soft: #6b5238;
    --serif-caps: "Cormorant Garamond", Georgia, serif;
    --serif-italic: "EB Garamond", Georgia, serif;
  }
  html, body { margin: 0; padding: 0; overflow: hidden; }
  body {
    width: 1200px; height: 800px;
    background: var(--backdrop);
    display: flex; align-items: center; justify-content: center; gap: 90px;
  }
  .card {
    position: relative;
    width: 300px; height: 490px;
    box-shadow: 0 14px 30px rgba(0,0,0,0.18);
  }

  /* Front */
  .card-front { background: var(--cream); color: var(--ink); }
  .front-rule {
    position: absolute; top: 74px; left: 108px; width: 84px; height: 2px;
    background: var(--gold);
  }
  .brand-name {
    position: absolute; top: 96px; left: 0; right: 0; text-align: center;
    font-family: var(--serif-caps); font-weight: 600;
    font-size: 18px; letter-spacing: 4px; line-height: 1.25;
    text-transform: uppercase; color: var(--ink);
  }
  .tagline {
    position: absolute; top: 168px; left: 0; right: 0; text-align: center;
    font-family: var(--serif-italic); font-style: italic;
    font-size: 15px; color: var(--ink-soft);
  }
  .contact {
    position: absolute; top: 252px; left: 40px;
    display: grid; grid-template-columns: 58px 1px auto; column-gap: 12px;
    font-family: var(--serif-italic); font-style: italic;
  }
  .contact-labels {
    text-align: right; font-size: 10px; color: var(--gold); line-height: 1;
  }
  .contact-labels span { display: block; }
  .contact-labels .l-address { margin-top: 12px; }
  .contact-labels .l-tel { margin-top: 26px; }
  .contact-labels .l-web { margin-top: 11px; }
  .contact-divider { background: var(--gold); width: 1px; height: 88px; }
  .contact-values { font-size: 11px; color: var(--ink); line-height: 1.3; }
  .contact-values p { margin: 0 0 8px; }
  .house-sketch {
    position: absolute; left: 40px; right: 24px; bottom: 28px; height: 100px;
    background: linear-gradient(180deg, rgba(74,29,21,0.08) 0%, rgba(74,29,21,0.55) 60%, rgba(62,42,28,0.25) 100%);
  }

  /* Back */
  .card-back { background: var(--umber); }
  .back-frame { position: absolute; inset: 0; }
  .back-rule {
    position: absolute; top: 196px; left: 58px; width: 2px; height: 100px;
    background: var(--gold);
  }
  .back-name {
    position: absolute; top: 212px; left: 74px;
    font-family: var(--serif-caps); font-weight: 600;
    font-size: 22px; letter-spacing: 5px; line-height: 1.25;
    text-transform: uppercase; color: var(--cream);
  }
  .back-tagline {
    position: absolute; top: 300px; left: 74px;
    font-family: var(--serif-italic); font-style: italic;
    font-size: 19px; color: var(--gold);
  }
</style>
</head>
<body>

  <section class="card card-front" aria-label="Business card front">
    <div class="front-rule"></div>
    <div class="brand-name">Willowmere<br>Loft</div>
    <div class="tagline">Bed &amp; Breakfast</div>

    <div class="contact">
      <div class="contact-labels">
        <span class="l-address">Address</span>
        <span class="l-tel">Tel.</span>
        <span class="l-web">Web</span>
      </div>
      <div class="contact-divider"></div>
      <div class="contact-values">
        <p>Brackleford, Hensworth<br>Somerset TA14 7QP</p>
        <p>01632 960418</p>
        <p>www.willowmereloft.co.uk</p>
      </div>
    </div>

    <div class="house-sketch" role="img" aria-label="Engraved sketch of the barn house beside a large tree"></div>
  </section>

  <section class="card card-back" aria-label="Business card back">
    <svg class="back-frame" width="300" height="490" viewBox="0 0 300 490" aria-hidden="true">
      <path d="M28,16 H272 A12,12 0 0 0 284,28 V462 A12,12 0 0 0 272,474 H28 A12,12 0 0 0 16,462 V28 A12,12 0 0 0 28,16 Z"
            fill="none" stroke="#c98a2a" stroke-width="1.5"/>
    </svg>
    <div class="back-rule"></div>
    <div class="back-name">Willowmere<br>Loft</div>
    <div class="back-tagline">Bed &amp; Breakfast</div>
  </section>

</body>
</html>
```